Bravik Telecom Branding and Visual Identity Project

We need some visual identity items for Bravik Telecom, which should be produced based on the company's logo attached.

I would like the brochure to be as lightweight as possible so that it can be sent via email.

Below are the items we need to be made.

- Company letterhead
- Company brochure in PDF format (single page)
- Email signature (only one)
- Wallpaper
- Banner for use on social media
- Customized shirt

Target Market(s)

Passengers and crew members of ships

Industry/Entity Type

Telecom & Maritime

Colors
0054AA
0677BA
7BADD7
CADEEF
E8F1F8

Requirements
Nice to have
• Colors that match the logo
Should not have
• Colors that clash with the logo colors

```html
<!DOCTYPE html>
<html lang="en">
<head>
<meta charset="utf-8">
<title>Bravik Telecom – Letterhead and Email Signature</title>
<link href="https://fonts.googleapis.com/css2?family=Roboto:wght@300;400;500&display=swap" rel="stylesheet">
<style>
  :root {
    --brand-blue: #0677BA;
    --brand-deep: #0054AA;
    --paper: #F6F4F4;
    --ink: #1d1d1d;
    --body-ink: #555555;
    --backdrop: #3b3b3b;
    --divider: #333333;
  }
  * { margin: 0; padding: 0; box-sizing: border-box; }
  html, body { width: 1200px; height: 853px; overflow: hidden; }
  body {
    background: var(--backdrop);
    font-family: "Roboto", Arial, sans-serif;
    position: relative;
    color: var(--ink);
  }
  .sheet {
    position: absolute;
    background: var(--paper);
    box-shadow: 0 4px 14px rgba(0,0,0,0.45);
  }
  .sheet-tab {
    position: absolute;
    top: 0;
    height: 7px;
    background: var(--brand-blue);
    border-radius: 0 0 4px 4px;
  }
  .brand {
    position: absolute;
    display: flex;
    align-items: center;
    gap: 6px;
    color: var(--brand-blue);
    font-weight: 500;
    white-space: nowrap;
  }
  .brand-mark {
    width: 10px; height: 10px;
    background: var(--brand-blue);
  }
  .contact-list { list-style: none; }
  .contact-list li {
    display: flex; align-items: center; gap: 4px;
    height: 12.5px;
  }
  .contact-list svg { width: 8px; height: 8px; flex: none; }
  .address { line-height: 12.5px; }

  /* Letterhead */
  .letterhead { left: 57px; top: 74px; width: 512px; height: 722px; }
  .letterhead .sheet-tab { left: 48px; width: 106px; }
  .letterhead .brand { left: 49px; top: 76px; font-size: 20px; }
  .letterhead .brand-mark { width: 12px; height: 12px; }
  .letterhead-contact {
    position: absolute; left: 355px; top: 48px;
    font-size: 10.2px; font-weight: 300; color: var(--ink);
  }
  .letterhead-contact .contact-list { margin-top: 3px; }
  .letter {
    position: absolute; left: 51px; top: 176px; width: 412px;
    color: var(--body-ink);
  }
  .salutation { font-size: 14.5px; font-weight: 400; color: #444; margin-bottom: 30px; }
  .letter p {
    font-size: 7.6px; line-height: 12.2px; font-weight: 300;
    text-align: justify; margin-bottom: 12.4px;
  }
  .closing { font-size: 8.4px; font-weight: 300; margin-top: 21px; }
  .signature-mark {
    width: 66px; height: 26px; margin: 8px 0 0 -2px;
    background: linear-gradient(90deg, rgba(40,40,40,0.15), rgba(40,40,40,0.05));
    border-radius: 3px;
  }
  .signer-name { font-size: 11.6px; font-weight: 400; color: #333; margin: 5px 0 0 3px; }
  .signer-title { font-size: 8.6px; font-weight: 300; margin: 2px 0 0 3px; }

  /* Email signature */
  .email-signature { left: 617px; top: 400px; width: 521px; height: 142px; }
  .email-signature .sheet-tab { left: 19px; width: 91px; }
  .email-signature .brand { left: 21px; top: 38px; font-size: 17px; }
  .sig-details {
    position: absolute; left: 21px; top: 89px;
    display: flex; font-size: 10.2px; font-weight: 300;
  }
  .sig-details .address { padding-right: 10px; border-right: 1px solid var(--divider); }
  .sig-details .contact-list { padding-left: 11px; }
</style>
</head>
<body>

<section class="sheet letterhead" aria-label="Letterhead">
  <div class="sheet-tab"></div>
  <div class="brand"><span class="brand-mark"></span>Bravik Telecom</div>

  <div class="letterhead-contact">
    <div class="address">2480 Harbor Light Rd<br>Suite 4B Port Alden<br>ME 04111</div>
    <ul class="contact-list">
      <li><svg viewBox="0 0 10 10"><path d="M2 1 L4 1 L4.8 3.3 L3.6 4.2 Q4.6 6 6 6.6 L6.9 5.4 L9 6.2 L9 8.2 Q5 9 2.4 5.6 Q1 3.4 2 1Z" fill="var(--brand-blue)"/></svg>2075550148</li>
      <li><svg viewBox="0 0 10 10"><rect x="0.5" y="2" width="9" height="6.5" fill="var(--brand-blue)"/><path d="M0.5 2 L5 5.6 L9.5 2" stroke="#fff" stroke-width="0.9" fill="none"/></svg>info@bravik.com</li>
      <li><svg viewBox="0 0 10 10"><circle cx="5" cy="5" r="4.5" fill="var(--brand-blue)"/><path d="M2.5 3.5 Q4 3 4.5 4.5 Q3.5 6 5.5 7" stroke="#fff" stroke-width="0.9" fill="none"/></svg>www.bravik.com</li>
    </ul>
  </div>

  <article class="letter">
    <h1 class="salutation">Dear Mr. Holm,</h1>
    <p>Lorem ipsum dolor sit amet, consectetur adipiscing elit. Donec orci purus, luctus vitae dignissim eu, iaculis sed purus. Vivamus faucibus, ipsum nec aliquet viverra, leo mauris condimentum ligula, sit amet sagittis enim ligula quis arcu. Nam egestas tortor id nisi porttitor mattis. In tortor ante, ultricies in suscipit a, tempus non massa. Vivamus et auctor mi. Fusce vel massa nulla. Phasellus nec eros mauris, et scelerisque orci.</p>
    <p>Donec malesuada orci vitae nulla accumsan porta a id massa. Quisque accumsan iaculis magna sit amet fringilla. Maecenas consequat, magna eget tincidunt semper, odio nibh rutrum mi, id feugiat ante nisi eu risus. Vestibulum nunc orci, rhoncus a placerat in, ultricies in mi. Cras mattis varius eros, vel fringilla nisi suscipit eget. Quisque scelerisque sagittis nulla at porttitor.</p>
    <p>Sed id augue vitae urna euismod commodo aliquet a quam. Pellentesque arcu velit, cursus et malesuada ut, consequat et diam. Nullam erat sem, rhoncus id ullamcorper vitae, rhoncus et arcu. In ultricies ultricies nulla, ut rutrum nisi iaculis at. Donec eu magna a metus ornare faucibus. Fusce aliquet faucibus ultricies. Morbi semper, est id tincidunt gravida, sem arcu adipiscing lacus, ac bibendum nulla leo eu purus. Quisque nec diam sed risus consectetur a ccumsan quis quis nibh. Vestibulum id purus lorem.</p>
    <p>It is a long established fact that a reader will be distracted by the readable content of a page when looking at its layout. The point of using Lorem Ipsum is that it has a more-or-less normal distribution of letters, as opposed to using 'Content here, content here', making it look like readable English. Many desktop publishing packages</p>
    <div class="closing">Sincerely,</div>
    <div class="signature-mark" role="img" aria-label="Handwritten signature"></div>
    <div class="signer-name">Daniel Varga</div>
    <div class="signer-title">CEO/ Founder</div>
  </article>
</section>

<section class="sheet email-signature" aria-label="Email signature">
  <div class="sheet-tab"></div>
  <div class="brand"><span class="brand-mark"></span>Bravik Telecom</div>
  <div class="sig-details">
    <div class="address">2480 Harbor Light Rd<br>Suite 4B Port Alden<br>ME 04111</div>
    <ul class="contact-list">
      <li><svg viewBox="0 0 10 10"><path d="M2 1 L4 1 L4.8 3.3 L3.6 4.2 Q4.6 6 6 6.6 L6.9 5.4 L9 6.2 L9 8.2 Q5 9 2.4 5.6 Q1 3.4 2 1Z" fill="var(--brand-blue)"/></svg>2075550148</li>
      <li><svg viewBox="0 0 10 10"><rect x="0.5" y="2" width="9" height="6.5" fill="var(--brand-blue)"/><path d="M0.5 2 L5 5.6 L9.5 2" stroke="#fff" stroke-width="0.9" fill="none"/></svg>info@bravik.com</li>
      <li><svg viewBox="0 0 10 10"><circle cx="5" cy="5" r="4.5" fill="var(--brand-blue)"/><path d="M2.5 3.5 Q4 3 4.5 4.5 Q3.5 6 5.5 7" stroke="#fff" stroke-width="0.9" fill="none"/></svg>www.bravik.com</li>
    </ul>
  </div>
</section>

</body>
</html>
```